Updated Business Card Design more modern and eye catching

looking for something more dynamic than the sterile card we have now. Please take a look at our web site www.brindlemarket.net to see what we do. only looking for the front side of the card for now. I've also attached a sample of a card with raised spot uv ink - it might be cool to incorporate something like that. Card should be bold yet serious. No frilly or scrolly stuff on it.
Updates
Target Market(s)
We do decor and signage for retail business and supermarkets. Our new name should reflect that we're hip but serious.
Contact Information for Business Card
standard business card size - horizontal preferred
Font styles to use
Requirements
Must have
- Current logo and colors cannot be changed.
Nice to have
- Must have information shown on existing card but open to some changes. Okay to consider spot uv.
Should not have
- Not busy with pictures in the background.

```html
<!DOCTYPE html>
<html lang="en">
<head>
<meta charset="utf-8">
<title>Brindle Market – Business Card</title>
<link href="https://fonts.googleapis.com/css2?family=Open+Sans:wght@400;600&family=Lora:ital@1&display=swap" rel="stylesheet">
<style>
  :root {
    --backdrop: #2a2d33;
    --card-black: #1c1c1c;
    --card-white: #ffffff;
    --gold: #b7a458;
    --gold-text: #a8913f;
    --ink: #1a1a1a;
    --logo-text: #c9b46a;
  }
  html, body {
    margin: 0;
    width: 1200px;
    height: 900px;
    overflow: hidden;
    background: var(--backdrop);
    font-family: "Open Sans", sans-serif;
  }
  .card {
    position: absolute;
    left: 180px;
    top: 210px;
    width: 840px;
    height: 480px;
    background: var(--card-black);
    overflow: hidden;
    box-shadow: 0 20px 50px rgba(0,0,0,.45);
  }
  .info-panel {
    position: absolute;
    left: 0; top: 0;
    width: 340px;
    height: 100%;
    background: var(--card-white);
  }
  .name {
    position: absolute;
    left: 40px; top: 42px;
    margin: 0;
    font-size: 30px;
    font-weight: 400;
    letter-spacing: .5px;
    color: var(--ink);
  }
  .title {
    position: absolute;
    left: 40px; top: 84px;
    width: 180px;
    padding-bottom: 6px;
    border-bottom: 1.5px solid var(--gold);
    font-family: "Lora", serif;
    font-style: italic;
    font-size: 17px;
    color: var(--gold-text);
  }
  .contacts {
    position: absolute;
    left: 40px; top: 140px;
    margin: 0; padding: 0;
    list-style: none;
    font-size: 18px;
    color: var(--ink);
  }
  .contacts li {
    display: flex;
    align-items: center;
    gap: 12px;
    height: 34px;
  }
  .contacts svg { width: 16px; height: 16px; fill: var(--gold); }
  .address-band {
    position: absolute;
    left: 0; top: 262px;
    width: 390px;
    height: 100px;
    background: var(--gold);
  }
  .address {
    position: absolute;
    left: 40px; top: 18px;
    display: flex;
    gap: 12px;
    font-size: 18px;
    line-height: 30px;
    color: var(--ink);
  }
  .address svg { width: 16px; height: 20px; margin-top: 5px; fill: var(--ink); }
  .website {
    position: absolute;
    left: 40px; top: 392px;
    font-size: 18px;
    color: var(--gold-text);
  }
  .brand {
    position: absolute;
    left: 430px; top: 205px;
    display: flex;
    align-items: center;
    gap: 16px;
  }
  .brand-square {
    width: 48px; height: 48px;
    border: 2px solid var(--logo-text);
    box-sizing: border-box;
  }
  .brand-name {
    font-size: 36px;
    font-weight: 400;
    letter-spacing: 4px;
    color: var(--logo-text);
  }
</style>
</head>
<body>
  <div class="card">
    <section class="info-panel">
      <h1 class="name">DANA HOLLIS</h1>
      <div class="title">Vice-President</div>
      <ul class="contacts">
        <li>
          <svg viewBox="0 0 16 16"><rect x="4" y="1" width="8" height="14" rx="1.5" fill="none" stroke="#b7a458" stroke-width="1.5"/></svg>
          555.210.4471
        </li>
        <li>
          <svg viewBox="0 0 16 16"><path d="M4 1l3 3-2 2c1 2 3 4 5 5l2-2 3 3-2 2C7 14 2 9 2 3z"/></svg>
          555.630.1185 ext.3
        </li>
        <li>
          <svg viewBox="0 0 16 16"><rect x="1" y="3" width="14" height="10" rx="1"/><path d="M1 4l7 5 7-5" fill="none" stroke="#fff" stroke-width="1.2"/></svg>
          dana@brindlemarket.net
        </li>
      </ul>
    </section>
    <div class="address-band">
      <div class="address">
        <svg viewBox="0 0 16 20"><path d="M8 0a7 7 0 0 0-7 7c0 5 7 13 7 13s7-8 7-13a7 7 0 0 0-7-7zm0 10a3 3 0 1 1 0-6 3 3 0 0 1 0 6z"/></svg>
        <div>140 Meridian Way<br>Fairhaven, FL 30210</div>
      </div>
    </div>
    <div class="website">www.brindlemarket.net</div>
    <div class="brand">
      <div class="brand-square"></div>
      <div class="brand-name">BRINDLE MARKET</div>
    </div>
  </div>
</body>
</html>
```